Book Title: Open Roads -- Finding Fellowship for a New Age

I am looking for just the book cover design, do not need spine or back cover art.

This book is a memoir and the cover needs to be prepared for print and ebook applications.

The part of the title that follows the dash ("Finding Fellowship for a New Age") is not a subtitle but a tag and can be separated from the title itself.

I am inclined to a traditional design with "modern and minimalist" tendencies. I like graphic images that convey the idea of a "journey" or "quest". The memoir is about my pastoral work as a Christian minister but it is not a "religious" book. I do not want churches or any traditional religious symbols on the cover. In fact this book is directed toward those who have little, if any, interest in organized religion of any kind and if that could somehow be captured in the cover art it would be useful.

I am attaching a file with some sample cover art designs that I like or do not like to help guide your thinking. I am open to your interpretation and creative thinking. This book is a labor of love and I want the cover art to reflect my deep thinking on the topic.

```html
<!DOCTYPE html>
<html lang="en">
<head>
<meta charset="UTF-8">
<title>Open Roads — Book Cover</title>
<link rel="stylesheet" href="https://fonts.googleapis.com/css2?family=Cinzel:wght@400;600;700&display=swap">
<style>
  :root {
    --backdrop: #cfd1d4;
    --title-teal: #12475f;
    --tag-ink: #17232c;
    --author-white: #fdf8ef;
    --sky-top: #eaf7fd;
    --sky-blue: #3fb4ea;
    --glow: #ffffff;
    --meadow: #a9b43a;
    --earth: #b4641f;
    --earth-deep: #7a3512;
  }
  html, body {
    margin: 0;
    padding: 0;
    width: 1200px;
    height: 972px;
    overflow: hidden;
    background: var(--backdrop);
  }
  .cover {
    position: absolute;
    left: 337px;
    top: 36px;
    width: 526px;
    height: 900px;
    overflow: hidden;
    font-family: "Cinzel", serif;
    box-shadow: 0 10px 30px rgba(0,0,0,0.18);
  }
  .cover-art {
    position: absolute;
    inset: 0;
    width: 100%;
    height: 100%;
  }
  .title {
    position: absolute;
    left: 0;
    right: 0;
    top: 56px;
    margin: 0;
    text-align: center;
    color: var(--title-teal);
    font-weight: 700;
    font-size: 104px;
    line-height: 128px;
    letter-spacing: 1px;
  }
  .title span { display: block; }
  .tagline {
    position: absolute;
    left: 0;
    right: 0;
    top: 348px;
    margin: 0;
    text-align: center;
    color: var(--tag-ink);
    font-weight: 400;
  }
  .tagline-main {
    display: block;
    font-size: 34px;
    line-height: 42px;
  }
  .tagline-link {
    display: flex;
    align-items: center;
    justify-content: center;
    gap: 12px;
    font-size: 19px;
    line-height: 32px;
  }
  .tagline-link::before,
  .tagline-link::after {
    content: "";
    width: 84px;
    height: 2px;
    background: var(--tag-ink);
  }
  .tagline-end {
    display: block;
    font-size: 40px;
    line-height: 50px;
  }
  .author {
    position: absolute;
    left: 0;
    right: 0;
    bottom: 44px;
    margin: 0;
    text-align: center;
    color: var(--author-white);
    font-size: 31px;
    font-weight: 400;
    letter-spacing: 0.5px;
  }
</style>
</head>
<body>
  <main class="cover">
    <svg class="cover-art" viewBox="0 0 526 900" preserveAspectRatio="none" role="img" aria-label="Bright sky with billowing blue clouds opening onto a glowing light, above a winding dirt road through a golden meadow">
      <defs>
        <linearGradient id="sky-to-earth" x1="0" y1="0" x2="0" y2="1">
          <stop offset="0" stop-color="var(--sky-top)"/>
          <stop offset="0.35" stop-color="#b7e4f8"/>
          <stop offset="0.62" stop-color="var(--sky-blue)"/>
          <stop offset="0.72" stop-color="#3d9fc8"/>
          <stop offset="0.78" stop-color="var(--meadow)"/>
          <stop offset="0.9" stop-color="var(--earth)"/>
          <stop offset="1" stop-color="var(--earth-deep)"/>
        </linearGradient>
        <radialGradient id="center-glow" cx="0.5" cy="0.62" r="0.42">
          <stop offset="0" stop-color="var(--glow)" stop-opacity="1"/>
          <stop offset="0.45" stop-color="var(--glow)" stop-opacity="0.75"/>
          <stop offset="1" stop-color="var(--glow)" stop-opacity="0"/>
        </radialGradient>
        <radialGradient id="road-warmth" cx="0.45" cy="0.9" r="0.35">
          <stop offset="0" stop-color="#e9a860" stop-opacity="0.8"/>
          <stop offset="1" stop-color="#e9a860" stop-opacity="0"/>
        </radialGradient>
      </defs>
      <rect width="526" height="900" fill="url(#sky-to-earth)"/>
      <rect width="526" height="900" fill="url(#road-warmth)"/>
      <rect width="526" height="900" fill="url(#center-glow)"/>
    </svg>

    <h1 class="title"><span>Open</span><span>Roads</span></h1>

    <p class="tagline">
      <span class="tagline-main">Finding Fellowship</span>
      <span class="tagline-link">for a</span>
      <span class="tagline-end">New Age</span>
    </p>

    <p class="author">Daniel M. Ashford</p>
  </main>
</body>
</html>
```